載内容詳細に関しては、別添のExcel資料を参照してください。

・ターゲット
BtoB
建設業の方で掘削の作業でお悩みのある方
→既存の建設現場が想像以上に地盤が固く、掘れないなど

くい打ち機をお探しの方
→金額が高いため、中古の需要が高い

・カラーイメージ

▼参考
https://www.torimo-haruka.jp/

・デザイン、ムード
見る方が50代~60第と年配の方が予想されるため、明朝体を使用し、堅めでしっかりした企業のイメージでデザインお願いします

▼参考
https://www.hoshinue-koki.com/

【素材】
▼ソラノハコ便
https://7.soranohako.jp/2811-a47f09c3b5e1d2886f04c71a9e5b2d03f

配置やデザイン等はアレンジしていただいて構いません。
また、縦に制限はありません。

レスポンシブデザインのサイトで、bootstrap4を利用しコーディングする予定になります。

デザイン幅は2000px、コンテンツの幅はbootstrap4デフォルトのの1110pxを基準としてください。
ただし、最近のデザインの流行を取りいれて、フルワイドや、1200~1500px程度の幅のコンテンツをバランスよくレイアウトしてください。
コンテンツ配置は基本12分割になります。がデザインによっては、多少逸脱してもかまいません。
bootstrap4、12分割グリッドの基準のPSDも資料として添付しております。
ご参考になさってください。

本分のフォントはゴシック系は游ゴシック、メイリオ、明朝系は遊明朝でお願いします。
飾り文字はフリーフォントか、googleフォントを利用してください。

メイン画像部分・グローバルメニューは、ワイド適用でお願いします。

不明点、質問などありましたらメッセージ等でご連絡ください。
1ページ
青系
• 高解像度JPG (.jpg)
• フォトショップ形式 (.psd)
・資料上はサイト名(社名)や住所などは伏字にしております。
ご提案時点ではそのまま作成をお願いします。

・使用画像は当選後こちらで用意します。
ご提案時点では前項同様に、カンプデータ等をご使用のうえ、当選後に本内容へ差し替え修正をお願いします。
また、雰囲気が合っていれば、指定外の画像を追加掲載いただいてOKです。

・当選前提となった方は正式な社名及び連絡先をお伝えしますので修正対応をお願いします。
また希望の際は、当選後、中ページの制作及びコーディングも別途ご依頼可能です。

```html
<!DOCTYPE html>
<html lang="ja">
<head>
<meta charset="utf-8">
<title>株式会社〇〇〇〇</title>
<link rel="stylesheet" href="https://fonts.googleapis.com/css2?family=Noto+Serif+JP:wght@400;600;700&family=Cormorant+Garamond:wght@500&family=Noto+Sans+JP:wght@400&display=swap">
<style>
:root{
  --navy:#1e3566;
  --navy-dark:#15254a;
  --ink:#2a2a2a;
  --muted:#666;
  --paper:#ffffff;
  --band:#efefef;
  --ghost:rgba(30,53,102,.10);
  --footer:#3a3a3a;
}
*{margin:0;padding:0;box-sizing:border-box}
html,body{width:1200px;height:2556px;overflow:hidden;background:var(--paper)}
body{font-family:"Noto Serif JP",serif;color:var(--ink);position:relative}
.abs{position:absolute}

/* header */
.header{position:absolute;top:0;left:0;width:1200px;height:44px;background:rgba(255,255,255,.92);z-index:3}
.logo{position:absolute;left:260px;top:12px;font-size:16px;font-weight:700;color:var(--navy)}
.nav{position:absolute;left:660px;top:15px;display:flex;gap:26px;font-size:11px;color:var(--ink)}
.nav-cta{position:absolute;left:940px;top:8px;width:100px;height:28px;background:var(--navy);color:#fff;font-size:11px;display:flex;align-items:center;justify-content:center}

/* hero */
.hero{position:absolute;top:0;left:0;width:1200px;height:600px;background:linear-gradient(120deg,#3a4a5c 0%,#2a3340 40%,#5a5040 60%,#2c3644 100%)}
.hero-shade{position:absolute;inset:0;background:linear-gradient(90deg,rgba(10,20,40,.55),rgba(10,20,40,.15))}
.hero-title{position:absolute;left:260px;top:290px;font-size:50px;line-height:1.3;font-weight:700;color:#fff;letter-spacing:2px}
.hero-sub{position:absolute;left:260px;top:430px;font-size:17px;font-weight:600;color:#fff}
.hero-sub small{font-size:12px}
.scroll{position:absolute;left:965px;top:395px;color:#fff;font-size:11px}
.scroll::after{content:"";position:absolute;left:4px;top:-50px;width:1px;height:45px;background:#fff}

/* ghost headings */
.ghost{position:absolute;font-family:"Cormorant Garamond",serif;font-size:118px;letter-spacing:6px;color:var(--ghost);white-space:nowrap;line-height:1}

/* section titles */
.sec-title{position:absolute;font-size:26px;font-weight:700;color:var(--ink);text-align:center}
.sec-title .en{display:block;font-family:"Cormorant Garamond",serif;font-size:11px;color:var(--navy);letter-spacing:2px;font-weight:500}
.btn{position:absolute;height:30px;background:var(--navy);color:#fff;font-size:10px;display:flex;align-items:center;justify-content:center;gap:8px}

/* company */
.company-photo{position:absolute;left:260px;top:660px;width:300px;height:360px;background:linear-gradient(160deg,#1d2c55,#2f4f8c 45%,#8aa7d8 55%,#1a2748)}
.company-text{position:absolute;left:600px;top:790px;width:330px;font-size:12px;line-height:1.9;color:var(--muted)}
.company-text p+p{margin-top:18px}

/* service */
.service{position:absolute;top:1270px;width:340px;height:250px;color:#fff;display:flex;flex-direction:column;align-items:center;justify-content:center;text-align:center}
.service.left{left:260px;background:linear-gradient(135deg,#2a4a8a,#3d6bb3)}
.service.right{left:600px;background:linear-gradient(160deg,#6b8db5,#2a4d7a 60%,#1d3b5e)}
.service h3{font-size:24px;font-weight:700}
.service .en{font-family:"Cormorant Garamond",serif;font-size:11px;margin:4px 0 10px}
.service p{font-size:10px;line-height:1.7;width:240px}
.service .more{margin-top:14px;width:110px;height:24px;border:1px solid #fff;font-size:10px;display:flex;align-items:center;justify-content:center}

/* products */
.products-band{position:absolute;top:1560px;left:0;width:1200px;height:340px;background:var(--band)}
.card{position:absolute;top:1690px;width:160px;height:120px;background:#fff;padding:8px}
.card .ph{width:144px;height:78px;background:linear-gradient(135deg,#4a4d55,#8a7a66)}
.card .cap{margin-top:8px;font-size:11px;text-align:center}

/* contact */
.contact-lead{position:absolute;left:0;width:1200px;top:2048px;text-align:center;font-size:11px;color:var(--muted)}
.tel-box{position:absolute;left:300px;top:2088px;width:270px;height:100px;border:1px solid var(--navy);text-align:center;padding-top:20px}
.tel-box .note{font-size:10px;color:var(--muted)}
.tel-box .num{font-size:22px;color:var(--navy);font-weight:600;margin-top:6px}
.mail-box{position:absolute;left:630px;top:2088px;width:270px;height:100px;background:var(--navy);color:#fff;display:flex;align-items:center;justify-content:center;gap:10px;font-size:12px}

/* footer */
.footer{position:absolute;top:2280px;left:0;width:1200px;height:276px;background:var(--footer);color:#ddd;text-align:center}
.footer .name{margin-top:46px;font-size:20px;font-weight:700;color:#fff}
.footer .addr{margin-top:14px;font-size:10px;line-height:1.8}
.footer .links{position:absolute;left:260px;top:160px;width:680px;display:flex;justify-content:space-between;font-size:10px;padding-top:16px;border-top:1px solid #555}
.footer .copy{position:absolute;left:0;bottom:0;width:1200px;height:36px;background:#2c2c2c;font-size:9px;line-height:36px;color:#aaa}
</style>
</head>
<body>

<section class="hero">
  <div class="abs" style="inset:0" role="img" aria-label="溶接作業を行う職人の写真"></div>
  <div class="hero-shade"></div>
  <h1 class="hero-title">お客様の要望を<br>カタチに。</h1>
  <p class="hero-sub">鋳鋼製品の設計・製作・改造、くい打ち機<small>の中古販売</small></p>
  <span class="scroll">1</span>
</section>

<header class="header">
  <div class="logo">株式会社〇〇〇〇</div>
  <nav class="nav"><span>ホーム</span><span>事業内容</span><span>製品例</span><span>会社概要</span></nav>
  <div class="nav-cta">お問い合わせ</div>
</header>

<!-- company -->
<div class="ghost" style="left:700px;top:635px">COMPANY</div>
<div class="company-photo" role="img" aria-label="溶接の火花が散る作業風景の写真"></div>
<h2 class="sec-title" style="left:600px;top:695px;text-align:left">会社概要<span class="en">COMPANY</span></h2>
<div class="company-text">
  <p>1960年の創業以来、<br>半世紀以上にわたり培った技術で、<br>高品質な鋳鋼製品をお届けしています。</p>
  <p>鋳鋼製品の設計・製作・改造から中古くい打ち機の販売まで幅広く対応しております。現場のお悩みに寄り添い、最適なご提案をいたします。どうぞお気軽にご相談ください。</p>
</div>
<div class="btn" style="left:820px;top:960px;width:120px">会社概要を見る ›</div>

<!-- service -->
<div class="ghost" style="left:330px;top:1085px">SERVICE</div>
<h2 class="sec-title" style="left:0;width:1200px;top:1195px">事業内容<span class="en">SERVICE</span></h2>
<div class="service left" role="img" aria-label="鋳鋼製品の写真">
  <h3>鋳鋼製品</h3><div class="en">Cast steel products</div>
  <p>設計から製作、改造までお客様のご要望に合わせて一貫して対応いたします。</p>
  <div class="more">詳しく見る ›</div>
</div>
<div class="service right" role="img" aria-label="くい打ち機の写真">
  <h3>くい打ち機中古販売</h3><div class="en">Used pile driver</div>
  <p>硬い地盤でも掘削可能なくい打ち機を、お手頃な価格でご提供いたします。</p>
  <div class="more">詳しく見る ›</div>
</div>

<!-- products -->
<div class="products-band"></div>
<div class="ghost" style="left:40px;top:1595px">PRODUCT EXAMPLE</div>
<h2 class="sec-title" style="left:0;width:1200px;top:1625px">製品例<span class="en">PRODUCT EXAMPLE</span></h2>
<div class="card" style="left:260px"><div class="ph" role="img" aria-label="製品写真"></div><div class="cap">オーガーヘッド</div></div>
<div class="card" style="left:433px"><div class="ph" role="img" aria-label="製品写真"></div><div class="cap">ビット</div></div>
<div class="card" style="left:606px"><div class="ph" role="img" aria-label="製品写真"></div><div class="cap">スクリュー</div></div>
<div class="card" style="left:780px"><div class="ph" role="img" aria-label="製品写真"></div><div class="cap">特殊部品</div></div>
<div class="btn" style="left:820px;top:1835px;width:120px">製品例一覧を見る ›</div>

<!-- contact -->
<div class="ghost" style="left:350px;top:1925px">CONTACT</div>
<h2 class="sec-title" style="left:0;width:1200px;top:1975px">お問い合わせ<span class="en">CONTACT</span></h2>
<p class="contact-lead">お見積り・ご相談など、お気軽にお問い合わせください。</p>
<div class="tel-box">
  <div class="note">お電話でのお問い合わせ</div>
  <div class="num">TEL 012-345-6789</div>
  <div class="note">受付時間 9:00〜17:00</div>
</div>
<div class="mail-box">
  <svg width="20" height="14" viewBox="0 0 20 14"><rect x="0.5" y="0.5" width="19" height="13" fill="none" stroke="#fff"/><path d="M1 1l9 7 9-7" fill="none" stroke="#fff"/></svg>
  メールでのお問い合わせ
</div>

<footer class="footer">
  <div class="name">株式会社〇〇〇〇</div>
  <div class="addr">〒000-0000 〇〇県〇〇市〇〇町1-2-3<br>TEL 012-345-6789 ／ FAX 012-345-6780</div>
  <div class="links"><span>ホーム</span><span>事業内容</span><span>鋳鋼製品</span><span>くい打ち機</span><span>製品例</span><span>会社概要</span><span>お問い合わせ</span></div>
  <div class="copy">Copyright © 株式会社〇〇〇〇 All Rights Reserved.</div>
</footer>

</body>
</html>
```